Talvex Engineering Business card Design

We need to make business cards for our NDT and inspection company. The company is called Talvex Engineering. We want a professional modern feel business card. We have just completed the remaking of our website and would like to have business cards with the same feel and colours. The final design should communicate professionalism and cutting edge tech.

Target Market(s)

We sell to B2B Business clients. Our customer is an engineer or decision maker in the mechanical engineering / Oil and gas field.

Contact Information for Business Card

Please see the current business cards that we have uploaded to get the details. You can also look at our Website www.talvex-eng.example for more.

Requirements
Must have
• Less is more
Nice to have
• Less is more

```html
<!DOCTYPE html>
<html lang="en">
<head>
<meta charset="utf-8">
<title>Talvex Engineering Business Card</title>
<link href="https://fonts.googleapis.com/css2?family=Open+Sans:wght@400;600;700&family=Arimo:wght@400;700&display=swap" rel="stylesheet">
<style>
  :root {
    --backdrop: #4a4a4c;
    --card: #1b1b1c;
    --ink: #ffffff;
    --ink-soft: #d6d6d6;
    --muted: #8a8a8a;
    --rule: #4a4a4a;
  }
  * { margin: 0; padding: 0; box-sizing: border-box; }
  html, body { width: 1200px; height: 1200px; overflow: hidden; }
  body {
    background: var(--backdrop);
    font-family: "Arimo", Arial, sans-serif;
    color: var(--ink);
    position: relative;
  }
  .card {
    position: absolute;
    left: 280px;
    width: 640px;
    height: 366px;
    background: var(--card);
    box-shadow: 0 14px 30px rgba(0,0,0,0.35);
  }
  .card--back { top: 200px; border-radius: 64px 0 64px 0; }
  .card--front { top: 630px; border-radius: 0 64px 0 64px; }

  /* Back side */
  .services { position: absolute; list-style: none; font-size: 17px; line-height: 23px; color: var(--ink-soft); }
  .services li::before { content: "\25CF"; font-size: 11px; margin-right: 6px; vertical-align: 2px; }
  .services--inspection { left: 56px; top: 52px; }
  .services--ndt { left: 400px; top: 92px; }
  .services--projects { left: 380px; top: 236px; }
  .back-rule { position: absolute; left: 56px; right: 40px; top: 282px; border-top: 1px solid var(--rule); }
  .tagline {
    position: absolute; left: 56px; top: 296px;
    font-family: "Open Sans", Arial, sans-serif; font-weight: 600;
    font-size: 16.5px; letter-spacing: 0.6px; color: var(--muted); text-transform: uppercase;
  }

  /* Front side */
  .brand { position: absolute; left: 40px; top: 64px; width: 260px; text-align: center; }
  .brand-mark { display: block; width: 92px; height: 92px; margin: 0 auto 14px; border-radius: 50%; background: var(--ink); }
  .brand-name {
    font-family: "Open Sans", Arial, sans-serif; font-weight: 700;
    font-size: 32px; line-height: 34px; text-transform: uppercase; color: var(--ink);
  }
  .divider { position: absolute; left: 326px; top: 52px; height: 220px; border-left: 1px solid var(--rule); }
  .person { position: absolute; left: 362px; top: 56px; }
  .person-name { font-weight: 700; font-size: 22px; letter-spacing: 0.4px; }
  .person-role { font-size: 16px; color: var(--ink-soft); margin-bottom: 12px; }
  .contact { list-style: none; font-size: 17px; line-height: 24px; color: var(--ink-soft); }
  .contact li { display: flex; align-items: center; gap: 6px; }
  .contact svg { width: 18px; height: 18px; flex: none; }
  .address { margin-top: 10px; font-size: 17px; line-height: 23px; color: var(--ink-soft); }
  .front-rule { position: absolute; top: 318px; border-top: 1px solid var(--rule); }
  .front-rule--left { left: 40px; width: 220px; }
  .front-rule--right { left: 346px; width: 230px; }
  .social { position: absolute; top: 300px; left: 268px; display: flex; gap: 8px; }
  .social span { width: 34px; height: 34px; border: 2px solid #666; border-radius: 50%; }
</style>
</head>
<body>
  <section class="card card--back" aria-label="Card back">
    <ul class="services services--inspection">
      <li>API 653 Tank Inspections</li>
      <li>API 570 Pipeline Inspections</li>
      <li>API 510 Pressure Vessel Inspections</li>
      <li>Welding Inspection</li>
      <li>Electrical Inspection</li>
      <li>OCTG Inspections</li>
      <li>Lifting Equipment Inspections</li>
    </ul>
    <ul class="services services--ndt">
      <li>Non-Destructive Testing</li>
      <li>UT/PT/MT/RT/VT</li>
      <li>Advanced NDT</li>
      <li>PAUT/MFL/ILI</li>
    </ul>
    <ul class="services services--projects">
      <li>Engineering Projects</li>
    </ul>
    <div class="back-rule"></div>
    <p class="tagline">We offer inspection &amp; engineering services</p>
  </section>

  <section class="card card--front" aria-label="Card front">
    <div class="brand">
      <span class="brand-mark"></span>
      <p class="brand-name">Talvex<br>Engineering</p>
    </div>
    <div class="divider"></div>
    <div class="person">
      <p class="person-name">SAMUEL OKOTH</p>
      <p class="person-role">Managing Director</p>
      <ul class="contact">
        <li><svg viewBox="0 0 18 18"><rect x="1" y="1" width="16" height="16" rx="2" fill="none" stroke="#d6d6d6" stroke-width="1.4"/><path d="M5 4.5l2 0 1 3-1.4 1a6 6 0 0 0 3 3l1-1.4 3 1v2a1 1 0 0 1-1 1A9 9 0 0 1 4 5.5a1 1 0 0 1 1-1z" fill="#d6d6d6"/></svg>+ 254 20 555 0142/3</li>
        <li><svg viewBox="0 0 18 18"><rect x="1" y="4" width="16" height="11" fill="none" stroke="#d6d6d6" stroke-width="1.4"/><path d="M1 4l8 6 8-6" fill="none" stroke="#d6d6d6" stroke-width="1.4"/></svg>info@talvex-eng.example</li>
        <li><svg viewBox="0 0 18 18"><circle cx="9" cy="9" r="7.5" fill="none" stroke="#d6d6d6" stroke-width="1.4"/><ellipse cx="9" cy="9" rx="3.3" ry="7.5" fill="none" stroke="#d6d6d6" stroke-width="1.2"/><path d="M1.5 9h15M3 5h12M3 13h12" stroke="#d6d6d6" stroke-width="1.2"/></svg>www.talvex-eng.example</li>
      </ul>
      <p class="address">P.O. BOX 40512-80100<br>Mombasa, Kenya</p>
    </div>
    <div class="front-rule front-rule--left"></div>
    <div class="social" aria-label="Social links"><span></span><span></span></div>
    <div class="front-rule front-rule--right"></div>
  </section>
</body>
</html>
```